Income Tax and Accounting Brochure

I need a brochure using my new logo (file attached). I do tax work and accounting work. I am an EA (QVX Enrolled Agent - logo attached) and would like this incorporated into the brochure. I also have a MSA in Accounting. Please incorporate the text that I have provided in the brochure.
Updates

Need extra days to review

Target Market(s)

Tax Clients - both business and individuals

Industry/Entity Type

Accounting

Colors
0054AA
0677BA
7BADD7
CADEEF
E8F1F8

Requirements
Must have
• Use my logo and the QVX EA file in the brochure
Nice to have
• I would like to see a brochure that I can customize with my own text if possible.

```html
<!DOCTYPE html>
<html lang="en">
<head>
<meta charset="utf-8">
<title>Halvern Accounting &amp; Consulting – Tax Planning Brochure</title>
<link rel="stylesheet" href="https://fonts.googleapis.com/css2?family=Montserrat:wght@600;700;800&family=Open+Sans:wght@400;600;700&display=swap">
<style>
  :root{
    --blue-deep:#0054AA;
    --blue:#0677BA;
    --blue-mid:#7BADD7;
    --blue-light:#CADEEF;
    --blue-pale:#E8F1F8;
    --red:#C8202B;
    --red-dark:#9E1820;
    --ink:#1D2F55;
    --white:#FFFFFF;
    --stage:#E4E7EB;
    --head:"Montserrat", sans-serif;
    --body:"Open Sans", sans-serif;
  }
  *{box-sizing:border-box;margin:0;padding:0}
  html,body{width:1200px;height:2400px;overflow:hidden}
  body{background:var(--stage);position:relative;font-family:var(--body);color:var(--ink)}
  .spread{position:absolute;left:60px;width:1080px;height:1000px;display:flex;box-shadow:0 10px 30px rgba(0,0,0,.18)}
  .spread--outside{top:90px}
  .spread--inside{top:1310px}
  .panel{position:relative;width:360px;height:1000px;overflow:hidden}
  .panel-bg{position:absolute;inset:0;width:100%;height:100%}
  .panel-content{position:absolute;inset:0}
  .photo{position:absolute}
  .web-pill{display:inline-flex;align-items:center;gap:8px;background:var(--red);color:var(--white);font:600 13px var(--body);padding:7px 18px;border-radius:20px}
  .web-pill .dot{width:12px;height:12px;border-radius:50%;border:2px solid var(--white)}

  /* About panel */
  .about{background:var(--white)}
  .about .badge{position:absolute;left:30px;top:250px;width:110px;height:44px;background:var(--blue-pale);border:2px solid var(--blue-mid);border-radius:4px}
  .about .portrait{position:absolute;left:178px;top:218px;width:140px;height:140px;border-radius:50%;border:5px solid var(--white);box-shadow:0 0 0 3px var(--blue);background:radial-gradient(circle at 50% 40%,#e7c9a9,#b98a64 70%,#7a5a44)}
  .about .text{position:absolute;left:30px;right:26px;top:392px}
  .about h3{font:800 21px var(--head);color:var(--blue-deep);text-transform:uppercase}
  .about .role{font:600 14px var(--body);color:var(--red);margin:4px 0 14px}
  .about p{font-size:13.5px;line-height:1.6;margin-bottom:14px}
  .about .tagline{font:700 14px var(--head);color:var(--blue)}
  .about .footer{position:absolute;left:0;right:0;bottom:26px;text-align:center}

  /* Intro panel */
  .intro{background:var(--red)}
  .intro .circle-photo{position:absolute;left:75px;top:50px;width:210px;height:210px;border-radius:50%;border:7px solid var(--white);background:radial-gradient(circle at 60% 55%,#d4a64a,#8b6a3a 55%,#4a4037)}
  .intro .text{position:absolute;left:30px;right:30px;top:300px;text-align:center;color:var(--white)}
  .intro p{font-size:14px;line-height:1.6;margin-bottom:16px}
  .intro h3{font:800 24px/1.2 var(--head);text-transform:uppercase;margin:26px 0 24px}
  .intro h4{font:700 16px var(--head);text-transform:uppercase;margin-bottom:10px}
  .intro address{font-style:normal;font-size:13.5px;line-height:1.6}
  .intro .footer{position:absolute;left:0;right:0;bottom:22px;text-align:center}

  /* Cover panel */
  .cover{background:var(--white)}
  .logo{position:absolute;left:34px;top:46px;display:flex;align-items:center;gap:12px}
  .logo-mark{width:50px;height:50px;border-radius:50%;background:var(--blue-deep)}
  .logo-name{font:700 19px/1.2 var(--head);color:var(--blue-deep);text-transform:uppercase}
  .cover .title{position:absolute;left:0;right:0;top:790px;text-align:center;color:var(--white)}
  .cover h1{font:800 46px var(--head);letter-spacing:1px}
  .cover .subtitle{font:600 23px var(--body);margin:4px 0 18px}

  /* Why hire us */
  .why{background:var(--blue-deep);color:var(--white)}
  .why .text{position:absolute;left:30px;right:28px;top:48px}
  .why h2{font:700 24px/1.2 var(--head);margin-bottom:16px}
  .why h2 span{display:block;font-weight:800}
  .why p{font-size:14px;line-height:1.6;margin-bottom:14px}

  /* Benefits */
  .benefits{background:var(--red);color:var(--white)}
  .benefits .text{position:absolute;left:26px;right:26px;top:40px}
  .benefits h2{font:800 20px var(--head);text-align:center;margin-bottom:26px;text-transform:uppercase}
  .benefit{display:flex;gap:14px;align-items:flex-start;margin-bottom:20px}
  .benefit svg{flex:0 0 46px}
  .benefit p{font-size:13px;line-height:1.55}
  .benefits .cta{text-align:center;margin-top:18px}
  .benefits .cta h3{font:800 17px/1.3 var(--head);text-transform:uppercase;margin-bottom:12px}
  .phone-pill{display:inline-flex;align-items:center;gap:8px;background:var(--white);color:var(--blue-deep);font:800 19px var(--head);padding:7px 24px;border-radius:22px}
  .benefits .closing{font-size:13px;line-height:1.55;text-align:center;margin-top:20px}
  .benefits .footer{position:absolute;left:0;right:0;bottom:18px;text-align:center}

  /* Bookkeeping */
  .books{background:var(--blue-deep);color:var(--white)}
  .books .text{position:absolute;left:30px;right:28px;top:380px}
  .books h2{font:700 26px/1.2 var(--head);margin-bottom:18px}
  .books h2 span{display:block;font-weight:800}
  .books p{font-size:14px;line-height:1.6;margin-bottom:14px}
  .books .footer{position:absolute;left:0;right:0;bottom:18px;text-align:center}
</style>
</head>
<body>

<!-- Outside of the trifold -->
<section class="spread spread--outside">

  <article class="panel about">
    <svg class="panel-bg" viewBox="0 0 360 1000" preserveAspectRatio="none">
      <defs>
        <linearGradient id="deskPhoto" x1="0" y1="0" x2="1" y2="1">
          <stop offset="0" stop-color="#d9dde3"/><stop offset="1" stop-color="#8d98a8"/>
        </linearGradient>
      </defs>
      <path d="M0 0H360V200C280 250 150 190 0 235Z" fill="url(#deskPhoto)" role="img" aria-label="Photo of colleagues reviewing financial papers at a desk"/>
      <path d="M0 235C150 190 280 250 360 200V214C280 262 150 204 0 250Z" fill="var(--blue)"/>
      <rect x="0" y="960" width="360" height="40" fill="var(--blue-pale)"/>
    </svg>
    <div class="panel-content">
      <div class="badge" role="img" aria-label="Enrolled agent credential badge"></div>
      <div class="portrait" role="img" aria-label="Portrait photo of the principal"></div>
      <div class="text">
        <h3>About Maren T. Ostrow</h3>
        <div class="role">MSA, EA (Principal)</div>
        <p>I have a Master's Degree in accounting and am a QVX Enrolled Agent. Enrolled Agents are the only tax professionals licensed by the federal government to represent taxpayers before the tax authority in all fifty states.</p>
        <p>I have experience working with a wide variety of clients, from those who have their first job to those who want to start a business. Taxes are complicated; let me help you make sense of them.</p>
        <div class="tagline">What's my fee to launch your success? Ask today.</div>
      </div>
      <div class="footer"><span class="web-pill"><span class="dot"></span>www.halvernaccounting.com</span></div>
    </div>
  </article>

  <article class="panel intro">
    <svg class="panel-bg" viewBox="0 0 360 1000" preserveAspectRatio="none">
      <path d="M0 420C120 360 250 470 360 400V700C240 770 120 640 0 720Z" fill="var(--red-dark)" opacity=".35"/>
      <path d="M0 940C120 900 240 960 360 920V1000H0Z" fill="var(--white)"/>
    </svg>
    <div class="panel-content">
      <div class="circle-photo" role="img" aria-label="Photo of an alarm clock, coin stacks and tax letter blocks"></div>
      <div class="text">
        <p>If you are looking for a blend of personal service and expertise, you have come to the right place. We offer a broad range of services for individuals, businesses and independent professionals.</p>
        <p>Our prices are affordable so you will get great value. We are experienced and friendly.</p>
        <h3>Contact us for a free consultation</h3>
        <h4>Contact Us</h4>
        <address>
          Halvern Accounting &amp; Consulting, LLC<br>
          4820 Bramble Ridge Rd, PO Box 18<br>
          Larkfield, VA 20191<br>
          Phone: (555) 014-2290<br>
          Fax: (555) 014-2291<br>
          office@halvernaccounting.com
        </address>
      </div>
      <div class="footer"><span class="web-pill"><span class="dot"></span>www.halvernaccounting.com</span></div>
    </div>
  </article>

  <article class="panel cover">
    <svg class="panel-bg" viewBox="0 0 360 1000" preserveAspectRatio="none">
      <defs>
        <linearGradient id="officePhoto" x1="0" y1="0" x2="1" y2="1">
          <stop offset="0" stop-color="#f2f3f5"/><stop offset=".6" stop-color="#c9ced6"/><stop offset="1" stop-color="#6f7a8c"/>
        </linearGradient>
      </defs>
      <path d="M0 140H360V560C300 640 200 680 0 700Z" fill="url(#officePhoto)" role="img" aria-label="Photo of two businesswomen reviewing documents in a bright office"/>
      <path d="M0 700C200 680 300 640 360 560V1000H0Z" fill="var(--red)"/>
      <path d="M0 740C190 700 300 640 360 600V1000H0Z" fill="var(--blue-deep)"/>
      <path d="M0 740C190 700 300 640 360 600V630C300 670 190 728 0 768Z" fill="var(--blue)"/>
    </svg>
    <div class="panel-content">
      <div class="logo">
        <span class="logo-mark"></span>
        <span class="logo-name">Halvern Accounting<br>Consulting, LLC</span>
      </div>
      <div class="title">
        <h1>TAX PLANNING</h1>
        <div class="subtitle">Income Tax &amp; Accounting</div>
        <span class="web-pill"><span class="dot"></span>www.halvernaccounting.com</span>
      </div>
    </div>
  </article>

</section>

<!-- Inside of the trifold -->
<section class="spread spread--inside">

  <article class="panel why">
    <svg class="panel-bg" viewBox="0 0 360 1000" preserveAspectRatio="none">
      <defs>
        <linearGradient id="meetingPhoto" x1="0" y1="0" x2="1" y2="1">
          <stop offset="0" stop-color="#8fa4bf"/><stop offset="1" stop-color="#2f3e57"/>
        </linearGradient>
      </defs>
      <path d="M0 760C120 720 240 790 360 740V1000H0Z" fill="url(#meetingPhoto)" role="img" aria-label="Photo of an advisor and a client discussing paperwork"/>
      <path d="M0 752C120 712 240 782 360 732V744C240 794 120 724 0 764Z" fill="var(--white)"/>
    </svg>
    <div class="panel-content">
      <div class="text">
        <h2>Tax Preparation<span>WHY HIRE US?</span></h2>
        <p>Preparing your own income tax return can be a task that leaves you with more questions than answers. According to a recent national survey, most taxpayers believe they benefited from using a professional tax preparer.</p>
        <p>Whether we like it or not, today's tax laws are so complicated that filing a relatively simple return can be confusing.</p>
        <p>It is just too easy to overlook deductions and credits to which you are entitled. Even if you use a computer software program, there's no substitute for the assistance of an experienced tax professional.</p>
      </div>
    </div>
  </article>

  <article class="panel benefits">
    <svg class="panel-bg" viewBox="0 0 360 1000" preserveAspectRatio="none">
      <path d="M0 955H360V1000H0Z" fill="var(--white)"/>
    </svg>
    <div class="panel-content">
      <div class="text">
        <h2>Here's what you get...</h2>
        <div class="benefit">
          <svg width="46" height="46" viewBox="0 0 46 46" fill="none" stroke="#fff" stroke-width="2"><circle cx="23" cy="23" r="21"/><rect x="15" y="12" width="16" height="22" rx="1"/><path d="M18 19h10M18 24h10M18 29h6"/></svg>
          <p>Your tax return will be checked and rechecked by our computer software, identifying potential problems the QVX may look at more closely.</p>
        </div>
        <div class="benefit">
          <svg width="46" height="46" viewBox="0 0 46 46" fill="none" stroke="#fff" stroke-width="2"><circle cx="23" cy="23" r="21"/><path d="M13 23h18M25 16l7 7-7 7"/></svg>
          <p>Your tax return can be filed electronically, so you will get a refund quicker.</p>
        </div>
        <div class="benefit">
          <svg width="46" height="46" viewBox="0 0 46 46" fill="none" stroke="#fff" stroke-width="2"><circle cx="23" cy="23" r="21"/><circle cx="23" cy="23" r="10"/><path d="M23 17v12M26 19.5c-1-1-5-1.5-5 1s5 1.5 5 4-4 2-5 1"/></svg>
          <p>Our staff will show you how to adjust your withholding so that you keep more money each month, not an interest-free loan to the government.</p>
        </div>
        <div class="benefit">
          <svg width="46" height="46" viewBox="0 0 46 46" fill="none" stroke="#fff" stroke-width="2"><circle cx="23" cy="23" r="21"/><path d="M14 23l6 6 12-12"/></svg>
          <p>We will point out potential deductions to lower your tax liability next year, so you can plan ahead with confidence.</p>
        </div>
        <div class="cta">
          <h3>Contact us for a<br>free consultation</h3>
          <span class="phone-pill">
            <svg width="18" height="18" viewBox="0 0 24 24" fill="var(--blue-deep)"><path d="M6.6 10.8a15.1 15.1 0 006.6 6.6l2.2-2.2c.3-.3.7-.4 1-.2 1.1.4 2.3.6 3.6.6.6 0 1 .4 1 1V20c0 .6-.4 1-1 1C10.6 21 3 13.4 3 4c0-.6.4-1 1-1h3.5c.6 0 1 .4 1 1 0 1.3.2 2.5.6 3.6.1.3 0 .7-.2 1z"/></svg>
            (555) 014-2290
          </span>
        </div>
        <p class="closing">We go beyond tax compliance and proactively recommend tax saving strategies to maximize your after-tax income.</p>
      </div>
      <div class="footer"><span class="web-pill"><span class="dot"></span>www.halvernaccounting.com</span></div>
    </div>
  </article>

  <article class="panel books">
    <svg class="panel-bg" viewBox="0 0 360 1000" preserveAspectRatio="none">
      <defs>
        <linearGradient id="cafePhoto" x1="0" y1="0" x2="1" y2="1">
          <stop offset="0" stop-color="#c7b59a"/><stop offset=".5" stop-color="#7f8f6a"/><stop offset="1" stop-color="#3d4a3a"/>
        </linearGradient>
      </defs>
      <path d="M0 0H360V300C240 350 120 290 0 340Z" fill="url(#cafePhoto)" role="img" aria-label="Photo of a woman reading papers at a cafe table"/>
      <path d="M0 340C120 290 240 350 360 300V314C240 364 120 304 0 354Z" fill="var(--white)"/>
      <path d="M0 955H360V1000H0Z" fill="var(--white)"/>
    </svg>
    <div class="panel-content">
      <div class="text">
        <h2>Books a Mess:<span>NO PROBLEM!</span></h2>
        <p>If you own a small business and haven't kept up your bookkeeping, don't worry. We can help you.</p>
        <p>We'll prepare your bookkeeping for the year, prepare a full Schedule C, as well as your personal income tax return.</p>
        <p>Then we'll help you set up an easy system that allows you to keep your books in tip-top shape next year.</p>
        <p>We make it a priority to enhance our mastery of the current tax code and new law changes, so you benefit from every update.</p>
      </div>
      <div class="footer"><span class="web-pill"><span class="dot"></span>www.halvernaccounting.com</span></div>
    </div>
  </article>

</section>

</body>
</html>
```